Vell Tarnmoor - Brochure - Industrial Construction Services

We need a brochure design based on the power point presentation attached. Our business is named Vell Tarnmoor and is an industrial project services business concentrating on Construction Project Management, Technical Services, and Consulting. We want to communicate that "We offer our clients a
unique systematic approach to solving technical challenges." As you can see from our logo designs we like the colors blue and grey. We are after clean, but innovative design overall. We also seem to like design that have darker style backgrounds. We would like this brochure to be a bi-fold 8.5"x 5.5" size when closed if possible. If any files or graphics are needed in original format please request them. Thanks!

Target Market(s)

Large Oil & Gas, Power Generation, and Engineering Companies.

Industry/Entity Type

Engineering

Font styles to use
Serif

Requirements
Must have
• A strong-lasting first impression.

```html
<!DOCTYPE html>
<html lang="en">
<head>
<meta charset="utf-8">
<title>Vell Tarnmoor – Brochure Spread</title>
<link rel="stylesheet" href="https://fonts.googleapis.com/css2?family=Tinos:ital,wght@0,400;0,700;1,700&family=Lato:ital@1&family=Roboto+Condensed:wght@700&display=swap">
<style>
  :root {
    --canvas: #e4e4e2;
    --page-white: #ffffff;
    --page-grey: #d9dadc;
    --brand-blue: #1668b0;
    --brand-blue-deep: #0d3f78;
    --brand-blue-light: #3f8fd6;
    --accent-red: #b3101c;
    --ink: #1b1b1b;
    --ink-grey: #4a4d52;
    --tag-blue: #1a4a8a;
    --tag-blue-light: #2f5fa8;
    --box-green: #a6d68a;
    --box-peach: #f2a98a;
    --box-sky: #b9d6f2;
    --arrow-grey: #9a9ca0;
  }
  html, body {
    margin: 0;
    width: 1200px;
    height: 900px;
    overflow: hidden;
    background: var(--canvas);
  }
  .brochure-spread {
    position: absolute;
    left: 50px;
    top: 92px;
    width: 1100px;
    height: 716px;
    box-shadow: 0 10px 28px rgba(0,0,0,0.28);
  }
  .brochure-spread svg { display: block; }
  .diagram-label { font-family: "Tinos", "Times New Roman", serif; fill: var(--ink); }
  .diagram-title { font-family: "Tinos", "Times New Roman", serif; font-weight: 700; fill: var(--ink); }
  .intro-copy { font-family: "Lato", Arial, sans-serif; font-style: italic; font-size: 21px; fill: var(--ink); }
  .contact-line { font-family: "Roboto Condensed", Arial, sans-serif; font-weight: 700; fill: #fff; }
  .contact-web { font-family: "Lato", Arial, sans-serif; fill: #fff; font-size: 21px; }
  .brand-name { font-family: "Tinos", "Times New Roman", serif; font-size: 24px; fill: var(--ink-grey); font-variant: small-caps; letter-spacing: 0.5px; }
  .brand-sub { font-family: "Tinos", "Times New Roman", serif; font-size: 9.5px; fill: var(--ink-grey); letter-spacing: 2px; }
  .tagline { font-family: "Tinos", "Times New Roman", serif; font-weight: 700; font-style: italic; font-size: 24px; font-variant: small-caps; }
</style>
</head>
<body>
<div class="brochure-spread">
  <svg width="1100" height="716" viewBox="0 0 1100 716" xmlns="http://www.w3.org/2000/svg">
    <defs>
      <linearGradient id="leftPageFill" x1="0" y1="0" x2="1" y2="0">
        <stop offset="0.55" stop-color="var(--page-white)"/>
        <stop offset="1" stop-color="var(--page-grey)"/>
      </linearGradient>
      <linearGradient id="rightPageFill" x1="0" y1="0" x2="1" y2="0">
        <stop offset="0" stop-color="var(--page-grey)"/>
        <stop offset="0.35" stop-color="var(--page-white)"/>
      </linearGradient>
      <linearGradient id="blueBand" x1="0" y1="0" x2="0" y2="1">
        <stop offset="0" stop-color="var(--brand-blue-light)"/>
        <stop offset="1" stop-color="var(--brand-blue-deep)"/>
      </linearGradient>
      <linearGradient id="crewPhotoTone" x1="0" y1="0" x2="0" y2="1">
        <stop offset="0" stop-color="#2b6db3" stop-opacity="0.2"/>
        <stop offset="0.5" stop-color="#3e78b8"/>
        <stop offset="1" stop-color="#1a5da6"/>
      </linearGradient>
      <radialGradient id="portraitTone" cx="0.4" cy="0.35" r="0.7">
        <stop offset="0" stop-color="#6d7a86"/>
        <stop offset="0.6" stop-color="#3c4650"/>
        <stop offset="1" stop-color="#1f2429"/>
      </radialGradient>
      <radialGradient id="projectCircle" cx="0.5" cy="0.35" r="0.65">
        <stop offset="0" stop-color="#9cbfe8"/>
        <stop offset="1" stop-color="#2f62b5"/>
      </radialGradient>
      <clipPath id="leftBlueClip">
        <path d="M0,0 L62,0 C80,380 240,640 550,716 L0,716 Z"/>
      </clipPath>
      <clipPath id="rightPageClip">
        <rect x="550" y="0" width="550" height="716"/>
      </clipPath>
      <marker id="arrowHeadBlack" viewBox="0 0 10 10" refX="5" refY="5" markerWidth="3.2" markerHeight="3.2" orient="auto">
        <path d="M0,0 L10,5 L0,10 Z" fill="#000"/>
      </marker>
    </defs>

    <!-- Left page -->
    <g class="page page-left">
      <rect x="0" y="0" width="550" height="716" fill="url(#leftPageFill)"/>
      <path class="accent-swoosh" d="M62,0 L112,0 C122,380 300,640 550,690 L550,716 C240,640 80,380 62,0 Z" fill="var(--accent-red)"/>
      <path d="M62,0 L74,0 C92,380 250,632 550,706 L550,716 C240,640 80,380 62,0 Z" fill="#fff"/>
      <path class="blue-panel" d="M0,0 L62,0 C80,380 240,640 550,716 L0,716 Z" fill="url(#blueBand)"/>
      <g clip-path="url(#leftBlueClip)" role="img" aria-label="Photo of engineers in hard hats working at an industrial control panel">
        <rect x="0" y="150" width="300" height="430" fill="url(#crewPhotoTone)"/>
      </g>

      <text class="contact-line" x="78" y="607" font-size="24">056-555-0148</text>
      <g class="icon-phone" transform="translate(54,588)" fill="#fff">
        <path d="M4,1 L8,1 L10,6 L7.5,8 C9,11 11,13 14,14.5 L16,12 L21,14 L21,18 C21,19.5 20,20 18.5,20 C9,19 2,12 1.5,3.5 C1.5,2 2.5,1 4,1 Z"/>
      </g>
      <text class="contact-web" x="54" y="638">www.velltarnmoor.com</text>

      <!-- Process diagram -->
      <g class="process-diagram">
        <circle cx="355" cy="150" r="105" fill="url(#projectCircle)" stroke="#6d94cc" stroke-width="2"/>
        <text class="diagram-title" x="355" y="68" font-size="14" text-anchor="middle" text-decoration="underline">PROJECT</text>
        <rect x="310" y="76" width="92" height="58" rx="4" fill="#c9ced4" role="img" aria-label="Illustration of an industrial processing plant with tanks and piping"/>
        <path d="M300,160 L318,146 L318,154 L392,154 L392,146 L410,160 L392,174 L392,166 L318,166 L318,174 Z" fill="var(--arrow-grey)" stroke="#6e7074" stroke-width="1"/>
        <text class="diagram-title" x="355" y="186" font-size="13" text-anchor="middle">Contract</text>

        <rect x="180" y="122" width="98" height="72" rx="8" fill="var(--box-green)" stroke="#7fb465"/>
        <text class="diagram-label" x="229" y="163" font-size="14" text-anchor="middle">CLIENT</text>

        <rect x="422" y="122" width="100" height="72" rx="8" fill="var(--box-peach)" stroke="#d9876a"/>
        <text class="diagram-label" x="472" y="147" font-size="11" text-anchor="middle">ENGINEERING</text>
        <text class="diagram-label" x="472" y="161" font-size="11" text-anchor="middle">&amp;</text>
        <text class="diagram-label" x="472" y="175" font-size="11" text-anchor="middle">CONSTRUCTION</text>

        <rect x="308" y="228" width="86" height="70" rx="8" fill="var(--box-sky)" stroke="#7fa7d3"/>
        <text class="diagram-label" x="351" y="260" font-size="12" text-anchor="middle" fill="var(--ink-grey)">Vell</text>
        <text class="diagram-label" x="351" y="275" font-size="12" text-anchor="middle" fill="var(--ink-grey)">Tarnmoor</text>

        <path d="M215,200 C220,245 255,262 296,264" fill="none" stroke="#000" stroke-width="9" marker-end="url(#arrowHeadBlack)"/>
        <path d="M402,266 C440,262 468,240 480,206" fill="none" stroke="#000" stroke-width="9" marker-end="url(#arrowHeadBlack)"/>

        <text class="diagram-title" x="352" y="318" font-size="14.5" text-anchor="middle">CONSTRUCTION PROJECT MANAGEMENT</text>
      </g>

      <text class="intro-copy" x="258" y="398">Lorem Ipsum is simply</text>
      <text class="intro-copy" x="258" y="426">dummy text of the printing</text>
    </g>

    <!-- Right page -->
    <g class="page page-right">
      <rect x="550" y="0" width="550" height="716" fill="url(#rightPageFill)"/>
      <line x1="550" y1="0" x2="550" y2="716" stroke="#c4c6c9" stroke-width="1"/>

      <g class="brand-lockup">
        <circle cx="722" cy="48" r="20" fill="var(--brand-blue)"/>
        <text class="brand-name" x="752" y="52">Vell Tarnmoor</text>
        <text class="brand-sub" x="753" y="69">MANAGEMENT &amp; CONSULTING</text>
      </g>

      <text class="tagline" x="838" y="132" text-anchor="middle"><tspan fill="var(--tag-blue)">Knowledge.</tspan><tspan fill="var(--ink)" dx="14">Integrity.</tspan><tspan fill="var(--tag-blue-light)" dx="14">Quality.</tspan></text>

      <g clip-path="url(#rightPageClip)">
        <circle cx="928" cy="478" r="318" fill="var(--brand-blue)"/>
        <circle cx="936" cy="482" r="302" fill="#fff"/>
        <circle cx="930" cy="480" r="290" fill="var(--brand-blue-deep)"/>
        <circle cx="940" cy="480" r="280" fill="#fff"/>
        <circle cx="944" cy="480" r="272" fill="url(#portraitTone)" role="img" aria-label="Portrait photo of the two company principals standing side by side"/>
      </g>
    </g>
  </svg>
</div>
</body>
</html>
```